Maplerun Co. Wordpress Design Project

Need a redesign of this site: http://www.themaplerunco.example/. Client wants to highlight before and after images of refinished furniture in some way that really showcases their work. Client deals with refurbishing low, middle and high end patio furniture and wants to appeal across the board. However, their bread and butter is in high end furniture refinishing. The home page should highlight everything found on their current home page including same navigation. Please show a dropdown under Residential. Use a combination of blue, white, yellow and maybe orange colors.
Updates

Reason: Client is slow to give any feedback.

Industry/Entity Type

Residential

Requirements
Must have
• Include a mini contact form on the home page. Phone number prominently displayed. Dropdown under Residential.
Nice to have
• You may feel free to use different colors in the logo in order to make it work with the design better.

```html
<!DOCTYPE html>
<html lang="en">
<head>
<meta charset="utf-8">
<title>The Maplerun Company</title>
<link rel="stylesheet" href="https://fonts.googleapis.com/css2?family=Source+Sans+3:wght@400;600;700&family=Open+Sans:wght@700;800&display=swap">
<style>
:root{
  --hero:#16304f;
  --hero-dark:#0f2440;
  --hero-line:#25456b;
  --nav-blue:#1f5f9e;
  --nav-blue-light:#3a82c4;
  --nav-border:#7fb3e0;
  --accent:#f2b632;
  --accent-orange:#e8862b;
  --blue-text:#1f5f9e;
  --blue-soft:#2f74b5;
  --page:#eef1f5;
  --panel:#f3f5f8;
  --ink:#2c3440;
  --muted:#8e97a3;
  --logo:#ffffff;
  --banner:#132a47;
  --banner-text:#ffffff;
  --white:#ffffff;
}
*{box-sizing:border-box;margin:0;padding:0}
html,body{width:1045px;height:1200px;overflow:hidden;background:var(--page)}
body{font-family:"Source Sans 3",sans-serif;color:var(--ink)}
.page{position:relative;width:1000px;height:1148px;transform:scale(1.045);transform-origin:0 0;
  background:repeating-linear-gradient(135deg,#f0f3f6 0 3px,#e9edf2 3px 5px)}
.abs{position:absolute}

.hero{left:0;top:0;width:1000px;height:415px;
  background:repeating-linear-gradient(90deg,rgba(255,255,255,.02) 0 2px,transparent 2px 6px),var(--hero)}
.topbar{left:0;top:0;width:1000px;height:72px;background:var(--hero-dark);border-bottom:1px solid var(--hero-line)}
.showcase{left:150px;top:92px;width:698px;height:323px;background:rgba(0,0,0,.16);box-shadow:0 0 30px rgba(0,0,0,.3)}

.brand-name{left:236px;top:2px;font-size:26px;line-height:29px;color:var(--logo);font-weight:400}

.nav-item{height:42px;top:15px;display:flex;align-items:center;justify-content:center;
  background:linear-gradient(var(--nav-blue-light),var(--nav-blue));border:1px solid var(--nav-border);
  color:var(--white);font-size:10px;font-weight:700;white-space:nowrap}
.nav-item.active{color:var(--accent)}
.dropdown{left:526px;top:44px;width:68px;height:57px;background:var(--hero-dark);border:1px solid var(--hero-line);
  display:flex;flex-direction:column;align-items:center;justify-content:space-around;padding:2px 0}
.dropdown span{font-size:10px;font-weight:600;color:var(--white)}
.dropdown span.current{color:var(--accent)}

.photo{top:100px;width:284px;height:280px;border:1px solid #3b5b80}
.photo.before{left:190px;background:linear-gradient(160deg,#6b4420,#8a5a2c 45%,#3a2414)}
.photo.after{left:532px;background:linear-gradient(160deg,#d9cfae,#efe6cd 45%,#b8ab88)}
.caption{top:378px;font-family:"Open Sans",sans-serif;font-weight:700;font-size:24px;color:var(--white);
  text-shadow:0 2px 3px rgba(0,0,0,.5)}

.banner{left:151px;top:415px;width:697px;height:58px;background:var(--banner);box-shadow:0 3px 6px rgba(0,0,0,.3)}
.banner-text{left:197px;top:427px;font-family:"Open Sans",sans-serif;font-weight:800;font-size:25px;color:var(--banner-text)}
.banner-text em{font-style:normal;color:var(--accent)}
.slider{left:750px;top:427px}

.feature{top:489px;width:221px;height:190px;background:var(--panel);border:1px solid var(--white);
  box-shadow:inset 0 0 12px rgba(0,0,0,.05);text-align:center;padding-top:14px}
.feature h2{font-size:22px;font-weight:400;color:var(--ink)}
.feature .lead{margin-top:14px;font-size:12px;color:var(--blue-text)}
.feature p.body{font-size:12px;line-height:14px;color:var(--muted);padding:2px 4px 0}
.btn{display:inline-flex;align-items:center;justify-content:center;height:25px;
  background:linear-gradient(#f7f8fa,#e3e7ec);border:1px solid #b6bec8;
  color:var(--blue-soft);font-size:12px;box-shadow:0 0 0 2px #f8f9fb inset}
.feature .btn{width:77px;margin-top:22px}

.contact-band{left:0;top:697px;width:1000px;height:291px;border-top:2px dotted #c6cdd6;border-bottom:1px solid #f6f8fa;
  background:repeating-linear-gradient(135deg,#dde3ea 0 3px,#d6dde5 3px 5px)}
.section-title{left:150px;top:716px;font-size:22px;font-weight:400}
.form-panel{left:149px;top:747px;width:470px;height:225px;background:var(--panel);border:1px solid var(--white)}
.label{font-size:12px;color:var(--ink)}
.field{background:var(--white);border:1px solid #cfd6de}
.info{font-size:12px;color:var(--ink)}

.testimonial{left:633px;top:747px;width:221px;height:224px;background:var(--panel);border:2px solid var(--white);
  box-shadow:inset 0 0 14px rgba(0,0,0,.07)}
.testimonial h3{position:absolute;left:22px;top:16px;font-size:18px;font-weight:400}
.quote-mark{position:absolute;left:14px;top:44px;font-family:"Open Sans",sans-serif;font-size:22px;font-weight:800;color:var(--accent)}
.quote{position:absolute;left:22px;top:54px;width:152px;font-size:9px;line-height:10.8px;color:var(--muted)}
.author{position:absolute;left:22px;top:161px;font-size:11px;color:var(--blue-text)}
.role{position:absolute;left:23px;top:175px;font-size:10px;color:#6f7884}

.footer-col{top:1005px}
.footer-col h4{font-size:10px;font-weight:400;color:var(--ink);margin-bottom:17px}
.footer-col ul{list-style:none}
.footer-col li{font-size:10px;color:var(--muted);height:22px}
.footer-col li::before{content:"";display:inline-block;width:3px;height:3px;background:var(--accent-orange);margin-right:6px;vertical-align:middle}
.copyright{left:681px;top:1005px;font-size:10px;line-height:10px;color:var(--muted)}
.copyright .policy{color:var(--blue-text)}
.social{top:1034px;width:24px;height:24px;background:linear-gradient(#f6f7f9,#dfe4ea);border:1px solid #c3cad3}
</style>
</head>
<body>
<div class="page">

  <div class="abs hero"></div>
  <div class="abs topbar"></div>
  <div class="abs showcase"></div>

  <div class="abs brand-name">The<br>Maplerun<br>Company</div>

  <nav>
    <div class="abs nav-item" style="left:469px;width:42px">HOME</div>
    <div class="abs nav-item active" style="left:529px;width:62px">RESIDENTIAL</div>
    <div class="abs nav-item" style="left:603px;width:60px">COMMERCIAL</div>
    <div class="abs nav-item" style="left:674px;width:47px">FABRICS</div>
    <div class="abs nav-item" style="left:729px;width:51px">ABOUT US</div>
    <div class="abs nav-item" style="left:790px;width:59px">CONTACT US</div>
    <div class="abs dropdown">
      <span class="current">OPTION 1</span><span>OPTION 1</span><span>OPTION 1</span>
    </div>
  </nav>

  <div class="abs photo before" role="img" aria-label="Worn oak corner cabinet before refinishing"></div>
  <div class="abs photo after" role="img" aria-label="Same corner cabinet refinished in cream after restoration"></div>
  <div class="abs caption" style="left:364px">Before</div>
  <div class="abs caption" style="left:724px">After</div>

  <div class="abs banner"></div>
  <div class="abs banner-text">DON’T REPLACE.. <em>RECYCLE..!!!!</em></div>
  <svg class="abs slider" width="104" height="31" viewBox="0 0 104 31">
    <rect x="1" y="1" width="102" height="29" rx="4" fill="#1f5f9e" stroke="#7fb3e0"/>
    <line x1="4" y1="9" x2="100" y2="9" stroke="#174c80"/>
    <line x1="4" y1="22" x2="100" y2="22" stroke="#174c80"/>
    <circle cx="30" cy="15" r="6" fill="none" stroke="#a9cdee"/>
    <circle cx="53" cy="15" r="8" fill="#f2b632"/>
    <circle cx="74" cy="15" r="6" fill="none" stroke="#a9cdee"/>
  </svg>

  <section>
    <div class="abs feature" style="left:151px">
      <h2>Welcome</h2>
      <p class="lead">Lorem Ipsum is simply dummy text</p>
      <p class="body">It is a long established fact that a reader will be distracted by the readable content of a page when looking at its layout. The point of using Lorem Ipsum is that it has a</p>
      <span class="btn">READ MORE</span>
    </div>
    <div class="abs feature" style="left:390px">
      <h2>What we do</h2>
      <p class="lead">Lorem Ipsum is simply dummy text</p>
      <p class="body">It is a long established fact that a reader will be distracted by the readable content of a page when looking at its layout. The point of using Lorem Ipsum is that it has a</p>
      <span class="btn">READ MORE</span>
    </div>
    <div class="abs feature" style="left:626px">
      <h2>Who we are</h2>
      <p class="lead">Lorem Ipsum is simply dummy text</p>
      <p class="body">It is a long established fact that a reader will be distracted by the readable content of a page when looking at its layout. The point of using Lorem Ipsum is that it has a</p>
      <span class="btn">READ MORE</span>
    </div>
  </section>

  <div class="abs contact-band"></div>
  <h2 class="abs section-title">Contact Us</h2>

  <div class="abs form-panel"></div>
  <div class="abs label" style="left:154px;top:774px">Name&nbsp;:</div>
  <div class="abs field" style="left:156px;top:797px;width:191px;height:20px"></div>
  <div class="abs label" style="left:154px;top:834px">E-Mail&nbsp;:</div>
  <div class="abs field" style="left:156px;top:857px;width:191px;height:20px"></div>
  <div class="abs label" style="left:154px;top:894px">Phone&nbsp;:</div>
  <div class="abs field" style="left:156px;top:917px;width:191px;height:20px"></div>
  <div class="abs label" style="left:363px;top:774px">Furniture That needs service :</div>
  <div class="abs field" style="left:363px;top:797px;width:246px;height:80px"></div>
  <span class="abs btn" style="left:369px;top:884px;width:77px">SUBMIT</span>
  <span class="abs btn" style="left:456px;top:884px;width:77px">CLEAR</span>
  <div class="abs info" style="left:363px;top:917px">Call us : Tollfree : 012-3456-700</div>
  <div class="abs info" style="left:363px;top:941px">E Mail : jhollis@maplerunrestore.example</div>

  <aside class="abs testimonial">
    <h3>Testimonials</h3>
    <span class="quote-mark">“</span>
    <p class="quote">Lorem Ipsum is simply dummy text of the printing and typesetting industry. Lorem Ipsum has been the industry's standard dummy text ever since the 1500s,Lorem Ipsum is simply dummy text of the printing and typesetting industry. Lorem Ipsum has been the industry's standard dummy text ever since the 1500s,</p>
    <div class="author">DANIEL HART</div>
    <div class="role">Senior Interior Designer</div>
  </aside>

  <footer>
    <div class="abs footer-col" style="left:151px"><h4>FOOTER 1</h4><ul><li>Sublink 1</li><li>Sublink 2</li><li>Sublink 3</li><li>Sublink 4</li></ul></div>
    <div class="abs footer-col" style="left:270px"><h4>FOOTER 2</h4><ul><li>Sublink 1</li><li>Sublink 2</li><li>Sublink 3</li><li>Sublink 4</li></ul></div>
    <div class="abs footer-col" style="left:389px"><h4>FOOTER 3</h4><ul><li>Sublink 1</li><li>Sublink 2</li><li>Sublink 3</li><li>Sublink 4</li></ul></div>
    <div class="abs copyright">Themapleruncompany@2012<br><span class="policy">Privacy policy</span></div>
    <div class="abs social" style="left:760px" aria-label="Social link"></div>
    <div class="abs social" style="left:791px" aria-label="Social link"></div>
    <svg class="abs social" style="left:824px" width="24" height="24" viewBox="0 0 24 24" aria-label="Email">
      <rect x="5" y="7" width="14" height="10" fill="none" stroke="#2c3440" stroke-width="1.4"/>
      <polyline points="5,7 12,13 19,7" fill="none" stroke="#2c3440" stroke-width="1.4"/>
    </svg>
  </footer>

</div>
</body>
</html>
```